Copperfox Billboard

Please design a billboard using my photos and logos.
For photo of truck please crop the truck itself out and not have the trees / dirt in photo.
Please put " Best Prices in Sevier County"
Please put " 30-yard Dumpsters Starting at 600.00"
Please put " 16-yard Dumpsters Starting at 300.0"
Please put " Delivery and Pickup 7 Days a week"
Billboard size will be 10 ft tall 30 ft wide

```html
<!DOCTYPE html>
<html lang="en">
<head>
<meta charset="utf-8">
<title>Copperfox Dumpsters Billboard</title>
<link rel="stylesheet" href="https://fonts.googleapis.com/css2?family=Oswald:wght@500;600;700&family=Montserrat:wght@500&display=swap">
<style>
  :root {
    --purple: #7f3b98;
    --purple-dark: #4a2468;
    --black: #000000;
    --white: #ffffff;
    --page: #ffffff;
  }
  * { margin: 0; padding: 0; box-sizing: border-box; }
  html, body { width: 1200px; height: 1200px; overflow: hidden; background: var(--page); }
  .canvas { position: relative; width: 1200px; height: 1200px; }
  .billboard {
    position: absolute; left: 16px; top: 404px; width: 1174px; height: 391px;
    background: var(--purple); overflow: hidden;
  }
  .billboard__bands { position: absolute; inset: 0; width: 100%; height: 100%; }
  .truck-photo {
    position: absolute; left: 62px; top: 6px; width: 410px; height: 244px;
    background: linear-gradient(90deg, #e9e9ec 0%, #d6d6da 45%, #3a2356 62%, #2e1a48 100%);
    border-radius: 6px;
  }
  .brand {
    position: absolute; left: 669px; top: 14px; width: 456px;
    font-family: "Oswald", sans-serif; font-weight: 700; color: var(--white);
    text-align: right; line-height: 1; white-space: nowrap;
  }
  .brand__name { display: block; font-size: 86px; letter-spacing: 2px; }
  .brand__sub { display: block; font-size: 40px; letter-spacing: 3px; margin-top: 4px; }
  .tagline {
    position: absolute; left: 620px; top: 168px; width: 550px; text-align: center;
    font-family: "Oswald", sans-serif; font-weight: 700; font-size: 34px; color: var(--white);
    line-height: 1; white-space: nowrap;
    transform: scaleX(0.9); transform-origin: center;
  }
  .service-pill {
    position: absolute; left: 46px; top: 290px; width: 496px; height: 63px;
    background: var(--purple); border-radius: 8px;
    display: flex; align-items: center; justify-content: center;
    font-family: "Oswald", sans-serif; font-weight: 700; font-size: 32px; color: var(--white);
    white-space: nowrap;
  }
  .offer { position: absolute; text-align: center; color: var(--white); white-space: nowrap; }
  .offer--30 { left: 675px; top: 269px; width: 200px; }
  .offer--16 { left: 928px; top: 289px; width: 200px; }
  .offer__icon { display: block; margin: 0 auto; background: var(--purple); border: 2px solid var(--purple-dark); }
  .offer--30 .offer__icon { width: 128px; height: 54px; }
  .offer--16 .offer__icon { width: 77px; height: 33px; }
  .offer__title {
    display: block; margin-top: 6px;
    font-family: "Oswald", sans-serif; font-weight: 700; font-size: 21px; line-height: 1.1;
  }
  .offer__price {
    display: block; margin-top: 2px;
    font-family: "Montserrat", sans-serif; font-weight: 500; font-size: 14px;
  }
</style>
</head>
<body>
<div class="canvas">
  <section class="billboard">
    <svg class="billboard__bands" viewBox="0 0 1878 626" preserveAspectRatio="none">
      <polygon points="0,143 895,143 1015,370 1878,370 1878,626 0,626" fill="#000000"/>
      <polyline points="13,168 880,168 998,383 1865,383" fill="none" stroke="#ffffff" stroke-width="26"/>
    </svg>
    <div class="truck-photo" role="img" aria-label="Photo of a white roll-off truck carrying a purple dumpster"></div>
    <div class="brand">
      <span class="brand__name">COPPERFOX</span>
      <span class="brand__sub">DUMPSTERS</span>
    </div>
    <p class="tagline">BEST PRICES IN SEVIER COUNTY</p>
    <p class="service-pill">Delivery and Pickup 7 Days a week</p>
    <div class="offer offer--30">
      <span class="offer__icon" role="img" aria-label="Illustration of a 30-yard dumpster"></span>
      <span class="offer__title">30-yard Dumpsters</span>
      <span class="offer__price">Starting @ 600.00"</span>
    </div>
    <div class="offer offer--16">
      <span class="offer__icon" role="img" aria-label="Illustration of a 16-yard dumpster"></span>
      <span class="offer__title">16-yard Dumpsters</span>
      <span class="offer__price">Starting @ 300.00"</span>
    </div>
  </section>
</div>
</body>
</html>
```